Business Card and Letterhead for Nurlo - modern real estate business

I need a double sided business card design for Nurlo. Please see business card brief here https://papers.trelvimo.net/sheet/q/7XrTbaLeZpMmQ2uWvd9HkCj4yNoEfsGi3lRtAz_pk/view?mode=shared

Please feel free to design the business cards however you feel best. I am happy to give some creative freedoms and then provide feedback from there.

Please then also create a letterhead to match the business card design

Colors

Designer to choose colors to be used in the design.

Requirements
Must have
• Must be a modern, elegant business card which looks very professional

```html
<!DOCTYPE html>
<html lang="en">
<head>
<meta charset="utf-8">
<title>Nurlo Business Card</title>
<link href="https://fonts.googleapis.com/css2?family=Roboto:wght@400;500;700&display=swap" rel="stylesheet">
<style>
  :root {
    --brand-red: #e31b23;
    --brand-red-deep: #d50d16;
    --ink: #4a4a4a;
    --paper: #ffffff;
    --backdrop: #d6d5d1;
    --photo-light: #e9e9ea;
    --photo-dark: #3a3d44;
  }
  * { box-sizing: border-box; margin: 0; padding: 0; }
  html, body { width: 1200px; height: 801px; overflow: hidden; }
  body {
    background: var(--backdrop);
    font-family: "Roboto", sans-serif;
    position: relative;
  }
  .card {
    position: absolute;
    top: 240px;
    width: 520px;
    height: 318px;
    box-shadow: 0 6px 18px rgba(0,0,0,0.18);
    overflow: hidden;
  }
  .card--front { left: 40px; background: var(--paper); }
  .card--back {
    left: 640px;
    background: linear-gradient(160deg, var(--brand-red) 0%, var(--brand-red) 60%, var(--brand-red-deep) 100%);
    display: flex;
    align-items: center;
    justify-content: center;
  }
  .wordmark {
    font-family: "Roboto", sans-serif;
    font-weight: 500;
    letter-spacing: 0.06em;
    line-height: 1;
  }
  .card--front .wordmark {
    position: absolute;
    top: 38px;
    left: 250px;
    font-size: 46px;
    color: var(--brand-red);
  }
  .card--back .wordmark {
    font-size: 104px;
    color: var(--paper);
  }
  .portrait {
    position: absolute;
    right: 0;
    bottom: 0;
    width: 230px;
    height: 200px;
    background: linear-gradient(180deg, var(--photo-light) 0%, #8c8f96 40%, var(--photo-dark) 100%);
  }
  .contact {
    position: absolute;
    left: 26px;
    bottom: 18px;
    font-size: 11.5px;
    line-height: 1.45;
    color: var(--ink);
  }
  .contact p { display: flex; align-items: center; gap: 6px; }
  .label { color: var(--brand-red); }
  .icon { width: 11px; height: 11px; flex: none; }
  .divider {
    width: 38px;
    height: 2px;
    background: var(--brand-red);
    margin: 10px 0 8px;
  }
  .agent-name {
    font-weight: 700;
    font-size: 17px;
    color: var(--brand-red);
    line-height: 1.2;
  }
  .agent-title {
    font-weight: 500;
    font-size: 14px;
    color: var(--ink);
    margin-bottom: 4px;
  }
</style>
</head>
<body>
  <section class="card card--front">
    <div class="wordmark">NURLO</div>
    <div class="portrait" role="img" aria-label="Portrait photo of the agent in a dark suit"></div>
    <div class="contact">
      <p>PO Box 5170</p>
      <p>Larkfield NSW 2790</p>
      <p><span class="label">Lic No.</span> 10473128</p>
      <p>
        <svg class="icon" viewBox="0 0 12 12"><path fill="#e31b23" d="M2.5 1 4.5 3 3.6 4.4c.7 1.6 2.3 3.2 4 4L9 7.5l2 2-1.4 1.5C5.5 10.6 1.4 6.5 1 2.4z"/></svg>
        02 4810 3927
      </p>
      <p>
        <svg class="icon" viewBox="0 0 12 12"><rect x="1" y="2.5" width="10" height="7" fill="none" stroke="#e31b23" stroke-width="1"/><path d="M1 2.5 6 6.5 11 2.5" fill="none" stroke="#e31b23" stroke-width="1"/></svg>
        info@nurlo.com
      </p>
      <p>
        <svg class="icon" viewBox="0 0 12 12"><circle cx="6" cy="6" r="5" fill="#e31b23"/></svg>
        www.nurlo.com
      </p>
      <div class="divider"></div>
      <p class="agent-name">Dane Carver</p>
      <p class="agent-title">Licenced Real Estate Agent</p>
      <p><span class="label">Lic No.</span> 20691845</p>
      <p>
        <svg class="icon" viewBox="0 0 12 12"><path fill="#e31b23" d="M2.5 1 4.5 3 3.6 4.4c.7 1.6 2.3 3.2 4 4L9 7.5l2 2-1.4 1.5C5.5 10.6 1.4 6.5 1 2.4z"/></svg>
        0451 386 209
      </p>
      <p>
        <svg class="icon" viewBox="0 0 12 12"><rect x="1" y="2.5" width="10" height="7" fill="none" stroke="#e31b23" stroke-width="1"/><path d="M1 2.5 6 6.5 11 2.5" fill="none" stroke="#e31b23" stroke-width="1"/></svg>
        dane@nurlo.com
      </p>
    </div>
  </section>

  <section class="card card--back">
    <div class="wordmark">NURLO</div>
  </section>
</body>
</html>
```